Simple and Clean business card design

We would like the design to be simple clean and to incorporate our colors.

We are open to your design and talent, we have the dots in our logo as we think of it as data points and we connect data points for people.

We are open to see the great creative and clean design you bring to the table

Contact Information for Business Card

please include: name, position, email, phone and website

Font styles to use
Sans Serif

Requirements
Must have
• my colors incorporated, simplicity
Nice to have
• lots of white space, simplicity
Should not have
• complexicity/ complex art

```html
<!DOCTYPE html>
<html lang="en">
<head>
<meta charset="utf-8">
<title>Nectra business card</title>
<link rel="stylesheet" href="https://fonts.googleapis.com/css2?family=Open+Sans:wght@400;600;700&display=swap">
<style>
  :root {
    --backdrop: #3b3b3d;
    --paper: #ffffff;
    --ink: #2b2b2b;
    --brand-red: #ea4335;
    --brand-yellow: #fbbc05;
    --brand-blue: #4285f4;
  }
  * { box-sizing: border-box; margin: 0; padding: 0; }
  html, body { width: 1200px; height: 1200px; overflow: hidden; }
  body {
    background: var(--backdrop);
    font-family: "Open Sans", sans-serif;
    position: relative;
  }
  .card {
    position: absolute;
    left: 182px;
    width: 836px;
    height: 479px;
    border-radius: 26px;
    overflow: hidden;
    box-shadow: 0 14px 22px rgba(0,0,0,0.45);
  }
  .card--front { top: 101px; background: var(--paper); }
  .card--back { top: 631px; background: var(--brand-blue); }

  .accent-band { position: absolute; inset: 0; width: 100%; height: 100%; }

  .wordmark {
    position: absolute;
    left: 80px;
    top: 68px;
    font-size: 92px;
    font-weight: 600;
    letter-spacing: 2px;
    color: var(--ink);
    line-height: 1;
  }
  .holder { position: absolute; left: 93px; top: 258px; color: var(--ink); }
  .holder__name { font-size: 31px; font-weight: 700; line-height: 1; }
  .holder__role { font-size: 24px; font-weight: 400; line-height: 1; margin-top: 1px; }

  .contacts { position: absolute; left: 64px; top: 337px; list-style: none; }
  .contacts__item {
    display: flex; align-items: center;
    font-size: 25px; color: var(--ink);
    height: 31px;
  }
  .contacts__icon { width: 18px; height: 18px; margin-right: 11px; flex: none; }

  .back-mark {
    position: absolute; inset: 0;
    display: flex; align-items: center; justify-content: center; gap: 20px;
    color: var(--paper);
    font-size: 104px; font-weight: 600; letter-spacing: 2px;
  }
  .back-mark__dot {
    width: 34px; height: 34px; border-radius: 50%; background: var(--paper);
  }
</style>
</head>
<body>

<section class="card card--front" aria-label="Card front">
  <svg class="accent-band" viewBox="0 0 836 479" preserveAspectRatio="none" aria-hidden="true">
    <rect x="640" y="0" width="196" height="479" fill="var(--brand-red)"/>
    <rect x="612" y="0" width="6" height="479" fill="var(--brand-yellow)"/>
  </svg>

  <div class="wordmark">Nectra</div>

  <div class="holder">
    <p class="holder__name">JOHN DOE</p>
    <p class="holder__role">owner</p>
  </div>

  <ul class="contacts">
    <li class="contacts__item">
      <svg class="contacts__icon" viewBox="0 0 20 20" aria-hidden="true">
        <rect x="1" y="4" width="18" height="12" fill="var(--brand-red)"/>
        <path d="M1 4 L10 11 L19 4 M1 16 L8 9.5 M19 16 L12 9.5" fill="none" stroke="#fff" stroke-width="1.4"/>
      </svg>
      hello@nectra-mail.com
    </li>
    <li class="contacts__item">
      <svg class="contacts__icon" viewBox="0 0 20 20" aria-hidden="true">
        <path d="M5 2 L8 2 L9 6 L7 8 C8 11 9.5 12.5 12 13.5 L14 11.5 L18 12.5 L18 15.5 C18 17 16.5 18 15 17.8 C8.5 17 3 11.5 2.2 5 C2 3.5 3 2 5 2 Z" fill="var(--brand-red)"/>
      </svg>
      0198 765 432
    </li>
    <li class="contacts__item">
      <svg class="contacts__icon" viewBox="0 0 20 20" aria-hidden="true">
        <circle cx="10" cy="10" r="8.5" fill="var(--brand-red)"/>
        <g fill="none" stroke="#fff" stroke-width="1.1">
          <ellipse cx="10" cy="10" rx="3.5" ry="8.5"/>
          <path d="M1.5 10 H18.5 M3 5.5 H17 M3 14.5 H17 M10 1.5 V18.5"/>
        </g>
      </svg>
      www.nectra.co
    </li>
  </ul>
</section>

<section class="card card--back" aria-label="Card back">
  <div class="back-mark">
    <span>Nectra</span>
    <span class="back-mark__dot"></span>
  </div>
</section>

</body>
</html>
```